依頼詳細
お客様に見積もり・図面などを提出する時に使用する封筒です。使用用途は幅広く、その他にも取引業者さまへのお手紙を出す時にも使います。

弊社は新築住宅・リフォーム工事を施工しているため、どちらのお客様にも使用できるよう、シンプルでかっこいいデザインをもとめています。
裏ありでも、なしでも構いません。

ロゴ添付しましたが、使用してもしなくても、構いません。

参考に弊社のホームページです

URL: https://www.bluecrestyuzawa.jp/
記載項目
北森燃料株式会社 住宅事業部 BLUE CREST
■下沢田ショールーム
〒048-2207
青森県三戸郡五戸町下沢田岡平34-8
■住宅事業部 本店事務所
〒048-2208
青森県三戸郡五戸町鶴間台柳原下平地52-6

※ここより下は2店の共通事項になります↓
TEL: 0178-94-7201 FAX: 0178-94-7216
Email: bluecrest.info@kitamori-nenryo.com
希望イメージ
シンプル 複雑
単色 カラフル
暗い 明るい
日常 高級
遊び心 厳粛
未来的 伝統的
女性的 男性的
希望する色
グレー系
納品ファイル
• イラストレーター形式 (.ai)
補足説明
ツバサプリント様にすぐ入稿できる形での納品をお願い致します。
※継続依頼あります。宜しくお願い致します。
■ 選んだ理由

『シンプルでかっこいい』という依頼通りのデザインでとても気に入りました。沢山デザインして頂き、ありがとうございます。丁寧で誠実な対応に感謝です。是非又何かありましたら、宜しくお願い致します。

■ 提案者全員のお礼・コメント

今回、報酬が安価に関わらず、沢山のランサー様が素敵なデザインを作成して頂きました!本当にありがとうございました。

```html
<!DOCTYPE html>
<html lang="ja">
<head>
<meta charset="utf-8">
<title>北森燃料株式会社 住宅事業部 角2封筒</title>
<link rel="stylesheet" href="https://fonts.googleapis.com/css2?family=Noto+Sans+JP:wght@400;500;700&display=swap">
<style>
  :root {
    --paper: #ffffff;
    --envelope-grey: #c9cac5;
    --forest: #1f4d36;
    --rule: #2c5a43;
    --ink-soft: #5e6a62;
  }
  html, body {
    margin: 0;
    padding: 0;
    width: 849px;
    height: 1200px;
    overflow: hidden;
    background: var(--paper);
    font-family: "Noto Sans JP", sans-serif;
  }
  .canvas {
    position: relative;
    width: 849px;
    height: 1200px;
  }
  .spec-note {
    position: absolute;
    left: 52px;
    top: 30px;
    font-size: 7px;
    letter-spacing: 0.05em;
    color: var(--ink-soft);
  }
  .envelope {
    position: absolute;
    left: 51px;
    top: 48px;
    width: 747px;
    height: 1112px;
    background: var(--envelope-grey);
  }
  .flap {
    position: absolute;
    left: 0;
    top: 0;
    width: 100%;
    height: 92px;
    background: var(--forest);
  }
  .flap-note {
    position: absolute;
    left: 0;
    right: 0;
    top: 66px;
    text-align: center;
    font-size: 7px;
    letter-spacing: 0.3em;
    color: #d9e2dc;
  }
  .house-frame {
    position: absolute;
    left: 0;
    top: 0;
  }
  .brand-name {
    position: absolute;
    left: 205px;
    top: 895px;
    width: 130px;
    font-weight: 700;
    color: var(--forest);
    text-align: center;
    line-height: 1.05;
  }
  .brand-name .word {
    display: block;
    font-size: 30px;
    letter-spacing: 0.18em;
  }
  .company-block {
    position: absolute;
    left: 375px;
    top: 877px;
    color: var(--forest);
    font-size: 7.5px;
    line-height: 1.55;
    letter-spacing: 0.04em;
  }
  .company-name {
    font-size: 11.5px;
    font-weight: 500;
    letter-spacing: 0.08em;
    margin: 0 0 6px;
  }
  .company-name .division { margin-left: 1.2em; }
  .office { margin: 0 0 5px; }
  .office-name { font-weight: 500; }
  .contact { margin: 0; }
</style>
</head>
<body>
<div class="canvas">
  <p class="spec-note">角2封筒 / 1色刷り / ダークグリーン</p>

  <div class="envelope">
    <div class="flap">
      <p class="flap-note">ここに糊付けしてください</p>
    </div>

    <svg class="house-frame" width="747" height="1112" viewBox="0 0 747 1112" aria-hidden="true">
      <polyline points="141,286 374,200 606,286" fill="none" stroke="var(--rule)" stroke-width="1"/>
      <rect x="141" y="286" width="465" height="694" fill="none" stroke="var(--rule)" stroke-width="1"/>
    </svg>

    <div class="brand-name">
      <span class="word">BLUE</span>
      <span class="word">CREST</span>
    </div>

    <div class="company-block">
      <p class="company-name">北森燃料株式会社<span class="division">住宅事業部</span></p>
      <div class="office">
        <div class="office-name">下沢田ショールーム</div>
        <div>〒048-2207</div>
        <div>青森県三戸郡五戸町下沢田岡平34-8</div>
      </div>
      <div class="office">
        <div class="office-name">住宅事業部　本店事務所</div>
        <div>〒048-2208</div>
        <div>青森県三戸郡五戸町鶴間台柳原下平地52-6</div>
      </div>
      <p class="contact">Tel. 0178-94-7201　Fax. 0178-94-7216</p>
      <p class="contact">Email. bluecrest.info@kitamori-nenryo.com</p>
      <p class="contact">https://www.bluecrestyuzawa.jp/</p>
    </div>
  </div>
</div>
</body>
</html>
```